LEAP GLIDE SOAR

Need a 4 X 6 post card design. Here are the elements that need to be on the card:
LEAP, GLIDE, SOAR (This is the title please feel free and create)
DATE: August 28, 2022
Showtimes 2:30 PM & 7:30 PM
Location: Harriet Colvane Theatre Walnut Creek, CA
Tickets can be purchased at:
http://colvanestagehall.tixora-example.com/LEAPGLIDESOAR or
by calling the ticket office at (925) 555-STAGE
LEAP, GLIDE, SOAR showcases the dance stylings of urban hip hop, ballet, modern jazz and much much more! Bay Area renown dancer/choreographer Rosa Janelle Pruitt headlines this cast of dancers and will amaze you as she takes you on a journey through dance that you will never forget. Join us for an experience that will prove to excite and delight you!
Now for the artwork I would like to incorporate all three of these photos. The photo entitled "beach" you are only to use the dancer on the left. So clip out the other dancer in the pink dress. The Garden photo and the beach photo the images need to be cut out from the background. The sidewalk photo you can leave the background (just my preference) but for the sake of the overall design I'm ok with removing its background as well.
Ok have at it. I want to end this competition in a few days so let's get these designs in. Thank you!

```html
<!DOCTYPE html>
<html lang="en">
<head>
<meta charset="utf-8">
<title>Leap Glide Soar – Postcard</title>
<link rel="stylesheet" href="https://fonts.googleapis.com/css2?family=Montserrat:wght@300;400;600;700&family=Great+Vibes&display=swap">
<style>
  :root {
    --page: #f4f4f4;
    --ink: #141414;
    --purple: #8e1a7e;
    --orange: #ee5a12;
    --amber: #f6a51a;
    --yellow: #f2e21c;
    --lime: #b7d63a;
    --green: #3fb36a;
    --pink: #ff2fb4;
    --cream: #fbf8ee;
    --band: rgba(20, 20, 20, 0.82);
  }
  * { margin: 0; padding: 0; box-sizing: border-box; }
  html, body { width: 800px; height: 1200px; overflow: hidden; background: var(--page); }
  body { position: relative; font-family: "Montserrat", Arial, sans-serif; color: var(--ink); }

  .postcard {
    position: absolute; left: 70px; width: 660px; height: 440px; overflow: hidden;
    box-shadow: 0 6px 14px rgba(0,0,0,0.18);
  }
  .postcard--front { top: 130px;
    background:
      radial-gradient(ellipse 40% 45% at 5% 8%, var(--purple) 20%, transparent 70%),
      radial-gradient(ellipse 45% 50% at 8% 95%, var(--orange) 30%, transparent 75%),
      radial-gradient(ellipse 35% 30% at 80% 2%, var(--amber) 20%, transparent 75%),
      radial-gradient(ellipse 40% 50% at 45% 85%, var(--green) 20%, transparent 75%),
      linear-gradient(110deg, var(--purple) 0%, var(--orange) 22%, var(--green) 42%, var(--lime) 58%, var(--yellow) 75%, var(--lime) 100%);
  }
  .postcard--back { top: 630px;
    background:
      radial-gradient(ellipse 45% 40% at 5% 95%, var(--orange) 10%, transparent 70%),
      radial-gradient(ellipse 60% 45% at 25% 85%, var(--amber) 10%, transparent 70%),
      radial-gradient(ellipse 35% 30% at 65% 5%, rgba(246,220,80,0.55) 10%, transparent 75%),
      radial-gradient(ellipse 40% 25% at 70% 98%, rgba(246,200,60,0.5) 10%, transparent 75%),
      var(--cream);
  }

  .photo { position: absolute; }
  .photo--dancer { left: 5%; top: 0; width: 33%; height: 100%;
    background: linear-gradient(180deg, rgba(90,55,40,0.55) 0%, rgba(25,20,20,0.75) 35%, rgba(20,20,20,0.8) 70%, rgba(70,45,35,0.55) 100%);
    border-radius: 40% 40% 10% 10% / 10% 10% 4% 4%; }
  .photo--headliner { right: 0; top: 6%; width: 17%; height: 94%;
    background: linear-gradient(180deg, rgba(60,40,35,0.8) 0%, var(--pink) 22%, var(--pink) 75%, rgba(255,100,200,0.6) 100%);
    border-radius: 45% 10% 0 0 / 12% 4% 0 0; }

  .title { position: absolute; line-height: 1; }
  .title__word { display: block; font-weight: 400; letter-spacing: 0.5px; }
  .title__script { display: block; font-family: "Great Vibes", cursive; }

  .front-title { left: 45%; top: 10%; }
  .front-title .title__word { font-size: 40px; margin-left: 62px; }
  .front-title .title__script { font-size: 78px; margin-top: -8px; }

  .event-details { position: absolute; left: 44%; top: 49%; display: flex; gap: 10px; font-weight: 700; }
  .event-details__col { line-height: 1; }
  .event-details__col--date { text-align: right; }
  .event-details__label { display: block; font-size: 10px; font-weight: 600; margin-bottom: 3px; }
  .event-details__label--date::before, .event-details__label--time::after {
    content: ""; display: inline-block; width: 50px; height: 1.5px; background: #fff; vertical-align: middle; margin: 0 4px;
  }
  .event-details__value { font-size: 20px; line-height: 1.05; }

  .location-band { position: absolute; left: 44%; top: 64%; width: 44%; padding: 5px 0 5px 10px;
    background: linear-gradient(90deg, transparent 0%, var(--band) 8%, var(--band) 80%, transparent 100%);
    color: #fff; font-size: 7.5px; font-weight: 700; }

  .tickets { position: absolute; right: 7%; top: 83%; text-align: right; font-weight: 700; line-height: 1.25; }
  .tickets__heading { font-size: 17px; }
  .tickets__line { font-size: 10.5px; }

  .back-title { left: 3%; top: 4%; }
  .back-title .title__word { font-size: 42px; margin-left: 64px; }
  .back-title .title__script { font-size: 82px; margin-top: -8px; }

  .description { position: absolute; left: 3.5%; top: 48%; width: 45%; font-size: 12.6px; font-weight: 400; line-height: 1.55; }

  .return-address { position: absolute; left: 54%; top: 9%; font-size: 7.5px; font-weight: 700; line-height: 1.5; }
  .stamp-box { position: absolute; left: 83%; top: 2.5%; width: 15%; height: 22.5%; border: 1px solid var(--ink); }
  .address-line { position: absolute; left: 54%; width: 44.5%; height: 1px; background: var(--ink); }
</style>
</head>
<body>

<section class="postcard postcard--front" aria-label="Postcard front">
  <div class="photo photo--dancer" role="img" aria-label="Cut-out photo of a dancer in a black leotard and skirt, arms raised in an arabesque"></div>
  <div class="photo photo--headliner" role="img" aria-label="Cut-out photo of the headlining choreographer in a pink dress"></div>

  <h1 class="title front-title">
    <span class="title__word">LEAP</span>
    <span class="title__word">GLIDE</span>
    <span class="title__script">Soar</span>
  </h1>

  <div class="event-details">
    <div class="event-details__col event-details__col--date">
      <span class="event-details__label event-details__label--date">DATE:</span>
      <span class="event-details__value">AUGUST 28<br>2022</span>
    </div>
    <div class="event-details__col">
      <span class="event-details__label event-details__label--time">SHOWTIMES</span>
      <span class="event-details__value">2:30 PM &amp;<br>7:30 PM</span>
    </div>
  </div>

  <p class="location-band">LOCATION: HARRIET COLVANE THEATRE WALNUT CREEK, CA</p>

  <div class="tickets">
    <p class="tickets__heading">Tickets can be purchased at:</p>
    <p class="tickets__line">http://colvanestagehall.tixora-example.com/LEAPGLIDESOAR or</p>
    <p class="tickets__line">by calling the ticket office at (925) 555-STAGE</p>
  </div>
</section>

<section class="postcard postcard--back" aria-label="Postcard back">
  <h2 class="title back-title">
    <span class="title__word">LEAP</span>
    <span class="title__word">GLIDE</span>
    <span class="title__script">Soar</span>
  </h2>

  <p class="description">showcases the dance stylings of urban hip hop, ballet, modern jazz and much much more! Bay Area renown dancer/choreographer Rosa Janelle Pruitt headlines this cast of dancers and will amaze you as she takes you on a journey through dance that you will never forget. Join us for an experience that will prove to excite and delight you!</p>

  <p class="return-address">1420 Lantern Way, Walnut Creek,<br>CA 94596, United States<br>+1 925-555-0183</p>

  <div class="stamp-box" aria-hidden="true"></div>
  <div class="address-line" style="top:47%"></div>
  <div class="address-line" style="top:56%"></div>
  <div class="address-line" style="top:65%"></div>
</section>

</body>
</html>
```